Delvin & Associates - London New Letting and Property Management Company *

Delvin & Associates LTD is a new company based in London, and works with brand new residential property in the city centre.

We are aiming to have 1000 new properties a year.

We are looking for something modern and minimalistic :
Logo ,Monogram, Paper Head and Business Card.

Target Market(s)

Internation landlords

Industry/Entity Type

Real Estate

Logo Text

Delvin & Associates

Colors

Designer to choose colors to be used in the design.

Requirements
Nice to have
• A particular monogram with "DA"
Should not have
• Little House over the logo

```html
<!DOCTYPE html>
<html lang="en">
<head>
<meta charset="utf-8">
<title>Delvin &amp; Associates — Stationery</title>
<link href="https://fonts.googleapis.com/css2?family=Open+Sans:wght@400;600&display=swap" rel="stylesheet">
<style>
  :root{
    --brand:#1f8fd8;
    --navy:#0a4f9a;
    --sky:#2ea6e6;
    --ink:#333;
    --muted:#666;
    --rule:#777;
    --paper:#fff;
  }
  *{margin:0;padding:0;box-sizing:border-box}
  html,body{width:1200px;height:1031px;overflow:hidden;background:#fff}
  body{position:relative;font-family:"Open Sans",Arial,sans-serif;color:var(--ink)}

  .brand-name{color:var(--brand);font-weight:600;letter-spacing:.06em;text-transform:uppercase;line-height:1.15}
  .brand-mark{display:inline-block;width:12px;height:12px;background:var(--brand)}

  .identity{position:absolute;left:170px;top:200px;width:200px;text-align:center}
  .identity .brand-mark{width:22px;height:22px;margin-bottom:14px}
  .identity .brand-name{font-size:17px}

  /* Letterhead */
  .letterhead{position:absolute;left:502px;top:63px;width:626px;height:882px;background:var(--paper);
    box-shadow:3px 4px 8px rgba(0,0,0,.35)}
  .letterhead .lh-logo{position:absolute;left:83px;top:100px;transform:translateY(-50%)}
  .letterhead .lh-logo .brand-name{font-size:11px}
  .lh-contact{position:absolute;right:52px;top:36px;list-style:none;text-align:right;font-size:10px;color:var(--muted);letter-spacing:.05em}
  .lh-contact li{height:14px;line-height:14px}
  .lh-contact li::after{content:"";display:inline-block;width:7px;height:6px;background:#7cc6ee;margin-left:8px;vertical-align:middle}
  .lh-rule{position:absolute;left:83px;right:53px;top:113px;height:2px;background:var(--rule)}
  .letter{position:absolute;left:83px;top:162px;width:465px;font-size:12.2px;line-height:21px;color:#444}
  .letter .recipient{margin-bottom:20px}
  .letter .body{text-align:justify;line-height:20.3px}
  .letter .signature{margin-top:22px}
  .lh-footer{position:absolute;left:0;right:0;top:811px;text-align:center;font-size:14px;color:#555}
  .lh-band{position:absolute;left:0;right:0;bottom:0;height:37px;background:var(--navy)}

  /* Business card */
  .card{position:absolute;left:64px;top:545px;width:376px;height:200px;background:var(--paper);
    box-shadow:3px 4px 8px rgba(0,0,0,.35);overflow:hidden}
  .card-top{position:absolute;left:0;top:0;right:0;height:93px;background:var(--navy)}
  .card-top .card-logo{position:absolute;left:32px;top:30px}
  .card-top .brand-name{font-size:8.5px;color:#8fd0f5}
  .card-top .brand-mark{background:#8fd0f5;width:9px;height:9px}
  .card-person{position:absolute;right:20px;top:52px;text-align:right;text-transform:uppercase}
  .card-person .name{font-size:12px;font-weight:600;color:#fff;letter-spacing:.03em}
  .card-person .title{font-size:10px;color:var(--sky);letter-spacing:.12em}
  .card-info{position:absolute;top:142px;font-size:10px;color:#333;line-height:15px;list-style:none}
  .card-info.left{left:14px}
  .card-info.right{right:14px;text-align:right}
  .card-info svg{width:9px;height:9px;vertical-align:middle;fill:var(--brand)}
  .card-info.left svg{margin-right:6px}
  .card-info.right svg{margin-left:5px}
  .card-band{position:absolute;left:0;bottom:0;width:376px;height:22px}
  .card-url{position:absolute;left:0;right:0;bottom:4px;text-align:center;color:#fff;font-size:10.5px}
</style>
</head>
<body>

<section class="identity" aria-label="Brand identity">
  <span class="brand-mark"></span>
  <div class="brand-name">Delvin &amp; Associates</div>
</section>

<section class="letterhead" aria-label="Letterhead">
  <div class="lh-logo"><div class="brand-name">Delvin &amp;<br>Associates</div></div>
  <ul class="lh-contact">
    <li>+44 (0) 207-5551</li>
    <li>+44 (0) 207-4444</li>
    <li>www.delvinassoc.com</li>
    <li>info@delvin.co.uk</li>
  </ul>
  <div class="lh-rule"></div>
  <div class="letter">
    <p class="recipient">Elena Marsh<br>Title<br>Company Name<br>18 Harbour Lane<br>Camden, London NW1<br>Date 1/30/12</p>
    <p class="body">Dear Elena,<br>
    Lorem ipsum dolor sit amet, consectetur adipiscing elit, set eiusmod tempor incidunt et labore et dolore magna aliquam. Ut enim ad minim veniam, quis nostrud exerc. Irure dolor in reprehend incididunt ut labore et dolore magna aliqua. Ut enim ad minim is nostrud exercitation ullam mmodo consequet. Duis aute in voluptate velit esse cillum dolore eu fugiat nulla pariatur.<br>
    At vver eos et accusam dignissum qui blandit est praesent. Lorem ipsum beynocguon doas nog apoply su trenz ucu hugh rasoluguon monugor et trenz ucugwo jag scannar. Wa hava laasad trenzsa gwo producgs su ldfoBraid, yop quiel geg ba solaly rasponsubla rof trenzur sala ent dusgrubuguon. Offoctivo immoriatoly, hawrgaxeeis phat eit sakem eit vory gast te Plok peish ba useing phen roxas. Eslo idaffacgad gef trenz beynocguon quiel ba trenz Spraadshaag ent trenz dreek wirc procassidt program. Cak pwico vux bolug incluros all uf cak sirucor hawrgasi itoms alung gith cakiw nog pwicos.<br>
    Plloaso mako nuto uf cakso dodtos anr koop a cupy uf cak vux noaw yerw phuno. Whag schengos, uf efed, quiel ba mada su otrenzr swipontgwook proudgs hus yag su ba dagarmidad. Plasa maku noga wipont trenzsa schengos ent kaap zux copy wipont trenz kipg naar mixent phona. Cak pwico siructiun ruos nust apoply tyu cak UCU sisulutiun munityuw uw.<br>
    Sincerely yours,</p>
    <p class="signature">Name Here</p>
  </div>
  <div class="lh-footer">London, UK, 77 Regent Street</div>
  <div class="lh-band"></div>
</section>

<section class="card" aria-label="Business card">
  <div class="card-top">
    <div class="card-logo"><span class="brand-mark"></span> <span class="brand-name">Delvin &amp; Associates</span></div>
    <div class="card-person"><div class="name">Persons Name</div><div class="title">Persons Title</div></div>
  </div>
  <ul class="card-info left">
    <li><svg viewBox="0 0 10 10"><path d="M2 0h2l1 3-1.5 1a6 6 0 0 0 2.5 2.5L7 5l3 1v2c0 1-1 2-2 2C4 10 0 6 0 2 0 1 1 0 2 0z"/></svg>(020) 555-0155</li>
    <li><svg viewBox="0 0 10 10"><rect x="2" y="0" width="6" height="10" rx="1"/></svg>(020) 555-0144</li>
  </ul>
  <ul class="card-info right">
    <li>info@delvin.co.uk<svg viewBox="0 0 10 10"><rect x="0" y="2" width="10" height="6"/></svg></li>
    <li>London, UK, 77 Regent Street<svg viewBox="0 0 10 10"><path d="M5 0a3.5 3.5 0 0 1 3.5 3.5C8.5 6 5 10 5 10S1.5 6 1.5 3.5A3.5 3.5 0 0 1 5 0z"/></svg></li>
  </ul>
  <svg class="card-band" viewBox="0 0 376 22" preserveAspectRatio="none" aria-hidden="true">
    <rect width="376" height="22" fill="var(--sky)"/>
    <polygon points="50,0 326,0 300,22 76,22" fill="var(--navy)"/>
  </svg>
  <div class="card-url">www.delvinassoc.com</div>
</section>

</body>
</html>
```